Real estate investor, needing a business card that communicates warmth, integrity, empathy.

I have a logo that can be manipulated to align with the message - "Serving your home selling needs." Want it to stand out from typical real estate investor cards, and make distressed home sellers feel a connection with me. Should communicate warmth, integrity, empathy, and trustworthiness.

Target Market(s)

Distressed home owners who need to sell their homes, not using realtors.

Contact Information for Business Card

Glossy front and matte back, with a small box that is labelled "notes." I like darker blues and blacks together, but doesn't have to be, as long as it communicates trustworthiness, and a strong call to action.

Other font styles liked:
• see "must haves" above, but willing to review whatever comes my way.

Requirements
Must have
• The fonts on my logo are Aviano, Lusitana, and Marcellus. We don't have to use those, but I favor them.

```html
<!DOCTYPE html>
<html lang="en">
<head>
<meta charset="utf-8">
<title>Harbor Lane Homes – Business Card</title>
<link href="https://fonts.googleapis.com/css2?family=Marcellus&family=Lusitana:wght@400;700&display=swap" rel="stylesheet">
<style>
  :root {
    --stage: #141517;
    --card-dark: #1f2226;
    --card-light: #ffffff;
    --ink: #1b1b1b;
    --paper-text: #f4f4f2;
    --copper: #a8794a;
    --dots: #333333;
  }
  * { margin: 0; padding: 0; box-sizing: border-box; }
  html, body {
    width: 1200px; height: 1189px; overflow: hidden;
    background: var(--stage);
  }
  .canvas {
    position: relative; width: 1200px; height: 1189px;
    display: flex; flex-direction: column; align-items: center; justify-content: center; gap: 40px;
  }
  .card {
    position: relative; width: 960px; height: 530px; border-radius: 34px; overflow: hidden;
  }

  /* Notes side */
  .card--notes { background: var(--card-light); color: var(--ink); }
  .card--notes .brand {
    position: absolute; top: 70px; left: 0; right: 0; text-align: center;
    font-family: "Marcellus", serif; font-size: 50px; letter-spacing: 3px; color: var(--ink);
  }
  .card--notes .notes-label {
    position: absolute; top: 175px; left: 0; right: 0; text-align: center;
    font-family: "Marcellus", serif; font-size: 30px; letter-spacing: 2px;
  }
  .notes-line {
    position: absolute; left: 90px; right: 90px; border-top: 3px dotted var(--dots);
  }
  .notes-line--one { top: 270px; }
  .notes-line--two { top: 340px; }
  .card--notes .tagline {
    position: absolute; top: 400px; left: 0; right: 0; text-align: center;
    font-family: "Lusitana", serif; font-size: 26px;
  }

  /* Contact side */
  .card--contact { background: var(--card-dark); color: var(--paper-text); }
  .card--contact .brand {
    position: absolute; top: 85px; right: 70px;
    display: flex; align-items: center; gap: 16px;
    font-family: "Marcellus", serif; font-size: 44px; letter-spacing: 2px; color: var(--paper-text);
  }
  .brand-dot { width: 18px; height: 18px; border-radius: 50%; background: var(--copper); }
  .person { position: absolute; left: 80px; top: 190px; }
  .person-name {
    font-family: "Marcellus", serif; font-size: 40px; letter-spacing: 2px; line-height: 1;
  }
  .person-title {
    margin-top: 6px; font-family: "Lusitana", serif; font-size: 26px; color: var(--copper);
  }
  .address {
    position: absolute; left: 90px; top: 290px;
    font-family: "Lusitana", serif; font-size: 24px; line-height: 1.3;
  }
  .contact-list { position: absolute; left: 90px; top: 375px; list-style: none; }
  .contact-list li {
    display: flex; align-items: center; gap: 14px;
    font-family: "Lusitana", serif; font-size: 23px; line-height: 1.45;
  }
  .contact-icon { width: 24px; height: 24px; flex: none; }
  .card--contact .tagline {
    position: absolute; left: 90px; bottom: 26px;
    font-family: "Lusitana", serif; font-size: 26px; letter-spacing: 1px;
  }
</style>
</head>
<body>
<main class="canvas">

  <section class="card card--notes" aria-label="Card back with notes area">
    <div class="brand">Harbor Lane Homes</div>
    <div class="notes-label">NOTE</div>
    <div class="notes-line notes-line--one"></div>
    <div class="notes-line notes-line--two"></div>
    <p class="tagline">Serving Your Home Selling Needs.</p>
  </section>

  <section class="card card--contact" aria-label="Card front with contact details">
    <div class="brand"><span class="brand-dot"></span>Harbor Lane Homes</div>

    <div class="person">
      <h1 class="person-name">DANIEL R. HALE</h1>
      <p class="person-title">Executive Director</p>
    </div>

    <p class="address">PO Box 456 Maple Avenue<br>Springfield, USA</p>

    <ul class="contact-list">
      <li>
        <svg class="contact-icon" viewBox="0 0 24 24" aria-hidden="true">
          <circle cx="12" cy="12" r="12" fill="#a8794a"/>
          <path d="M8 6.5l2 0 1 3-1.3 1a7 7 0 0 0 3.8 3.8l1-1.3 3 1v2a1.5 1.5 0 0 1-1.6 1.5A10 10 0 0 1 6.5 8.1 1.5 1.5 0 0 1 8 6.5z" fill="#1f2226"/>
        </svg>
        555-204-1187
      </li>
      <li>
        <svg class="contact-icon" viewBox="0 0 24 24" aria-hidden="true">
          <circle cx="12" cy="12" r="12" fill="#a8794a"/>
          <rect x="6" y="8" width="12" height="8.5" fill="none" stroke="#1f2226" stroke-width="1.5"/>
          <path d="M6 8l6 5 6-5" fill="none" stroke="#1f2226" stroke-width="1.5"/>
        </svg>
        info@harborlanehomes.com
      </li>
      <li>
        <svg class="contact-icon" viewBox="0 0 24 24" aria-hidden="true">
          <circle cx="12" cy="12" r="12" fill="#a8794a"/>
          <circle cx="12" cy="12" r="6" fill="none" stroke="#1f2226" stroke-width="1.3"/>
          <ellipse cx="12" cy="12" rx="2.6" ry="6" fill="none" stroke="#1f2226" stroke-width="1.3"/>
          <path d="M6 12h12" stroke="#1f2226" stroke-width="1.3"/>
        </svg>
        www.harborlanehomes.com
      </li>
    </ul>

    <p class="tagline">SERVING YOUR HOME SELLING NEEDS.</p>
  </section>

</main>
</body>
</html>
```